Emerging Education Provider Needs a Contemporary and Compelling Promotional Presentation

We are Juniper Learning and Skills Institute, a privately owned institution that is really going places. We offer a range of Diploma, Language and Short courses for both Domestic and International students with both face to face delivery and on-line or blended. We currently run out of two campuses in Brisbane (Queensland Australia) one in the heart of the city and one in the multi-cultural precinct of Bellhaven Rise. We are currently expanding with additional campuses planned for the Gold Coast and for Melbourne, Victoria.
Please refer to our web site jlsi-example.edu.au.
We need a promotional presentation (doesn't necessarily have to be in PowerPoint) to promote our business - It really needs to pop!
Proposed Pack:
Opening slide
Content & Agenda
CEO Welcome
Mission and Vision
Our Values
Why Choose JLSI (multiple slides)
Our Campuses (Brisbane, Bellhaven Rise, In Development)
Life in Brisbane (2 slides - Queensland and Brisbane)
Our Courses (3 slides - Domestic, International, On-Line)
Student Services (multiple slides)
How to Apply
Closing Slide
Updates

Reason: I will be travelling and unable to review submissions until early next week. Can all submissions please ensure the pack has a real wow factor. This will be a pack that we will have on a big screen at a trade show where thousands of people are walking by. The presentation needs to get people to stop and watch. So no graphs or data, few words per slide, lots of compelling images, a real contemporary feel.

Target Market(s)

Educational institutions, prospective students, Business to Business, seminars and trade shows.

Industry/Entity Type

Education

Font styles to use
Sans Serif

Colors
a54499

Requirements
Must have
• Consistent with our branding theme / colours.
• Template + content using information from our International Prospectus and web site.
• Delineation between domestic and international offerings.
• Showcasing the beautiful location from which we operate.
Nice to have
• Ability to utilise the presentation for generation of other marketing collateral (flyers, posters) in future.
• Cut in video footage of our location (Queensland, Brisbane, Gold Coast).
• Any general content / slides / video that may inspire travel to Australia to study or participation in study.
Should not have
• Be off-brand.

```html
<!DOCTYPE html>
<html lang="en">
<head>
<meta charset="utf-8">
<title>Our Vision</title>
<link rel="stylesheet" href="https://fonts.googleapis.com/css2?family=Open+Sans:wght@400;800&display=swap">
<style>
  :root {
    --sky-top: #1f5a73;
    --sky-mid: #4fa9c9;
    --sky-light: #c9e3ea;
    --rock: #8a8f8c;
    --forest-dark: #1f3a22;
    --forest-light: #6f9a3a;
    --band: rgba(38, 38, 36, 0.82);
    --text: #ffffff;
  }
  html, body {
    margin: 0;
    padding: 0;
    width: 1200px;
    height: 804px;
    overflow: hidden;
    background: #ffffff;
  }
  .slide {
    position: relative;
    width: 1200px;
    height: 804px;
    overflow: hidden;
    font-family: "Open Sans", sans-serif;
    color: var(--text);
  }
  .slide__backdrop {
    position: absolute;
    inset: 0;
    background:
      linear-gradient(180deg,
        var(--sky-top) 0%,
        var(--sky-mid) 18%,
        var(--sky-light) 36%,
        var(--rock) 46%,
        var(--forest-dark) 62%,
        var(--forest-dark) 80%,
        var(--forest-light) 100%);
  }
  .slide__title {
    position: absolute;
    top: 58px;
    left: 0;
    width: 100%;
    margin: 0;
    text-align: center;
    font-weight: 800;
    font-size: 64px;
    letter-spacing: 1px;
    text-shadow: 0 2px 6px rgba(0, 0, 0, 0.35);
  }
  .vision-band {
    position: absolute;
    top: 461px;
    left: 0;
    width: 100%;
    height: 184px;
    background: var(--band);
    display: flex;
    align-items: center;
    justify-content: center;
  }
  .vision-band__statement {
    margin: 0;
    width: 1120px;
    text-align: center;
    font-weight: 400;
    font-size: 33px;
    line-height: 1.3;
    padding-bottom: 12px;
  }
</style>
</head>
<body>
  <main class="slide">
    <div class="slide__backdrop" role="img" aria-label="Mountain valley landscape with granite cliffs, a waterfall, cloudy blue sky and pine forest"></div>
    <h1 class="slide__title">OUR VISION</h1>
    <section class="vision-band">
      <p class="vision-band__statement">Empowering people to become persons of influence and support&shy;ing our local community and beyond</p>
    </section>
  </main>
</body>
</html>
```